Web design for Modeling agency

We are looking for re-designing our modeling agency website.
Current website: lunafaces.com our competitor: KTRfaces.com
http://brisaface.fr/
https://www.corvelmanagement.com/models/
https://www.hedwig-faces.de
https://www.rustmanagement.co.uk
https://www.quorbfaces.com
https://www.harborlightfaces.com

Target Market(s)

modeling agency

Industry/Entity Type

modeling agency

Number of Pages Required

5+ page

Font styles to use
Other font styles liked:
• base on logo guidline

Requirements
Nice to have
• current website: lunafaces.com our competitor: KTRfaces.com

```html
<!DOCTYPE html>
<html lang="en">
<head>
<meta charset="utf-8">
<title>Luna Model Mgmt</title>
<link rel="stylesheet" href="https://fonts.googleapis.com/css2?family=Montserrat:wght@400;500;600;700&family=Playfair+Display:wght@400&family=Hind:wght@700&display=swap">
<style>
:root{
  --brand:#b58a6e;
  --ink:#1a1a1a;
  --band:rgba(40,30,25,.82);
  --band-text:#c9a58c;
  --rule:#333;
  --accent-line:#c9a58c;
  --deco:#e4e8f5;
  --brown-top:#6d4b37;
  --brown-mid:#b5845f;
  --promo-copy:#f7dcc6;
  --white:#fff;
}
*{margin:0;padding:0;box-sizing:border-box}
html,body{width:1200px;height:3000px;overflow:hidden;background:var(--white)}
body{position:relative;font-family:"Montserrat",sans-serif;color:var(--ink)}
.abs{position:absolute}
.icon-dot{width:35px;height:35px;border-radius:50%;background:var(--brand);display:flex;align-items:center;justify-content:center}
.contact{font-size:15px;font-weight:500;line-height:23px;white-space:nowrap}
.logo{text-align:center;color:var(--brand);font-family:"Playfair Display",serif;font-weight:400;line-height:1;white-space:nowrap}
.logo .name{font-size:58px;letter-spacing:2px}
.logo .sub{font-size:22px;letter-spacing:1px;margin-top:6px}
.rule{left:172px;width:856px;top:136px;height:1px;background:var(--rule)}
.nav{top:162px;left:0;width:1200px;display:flex;justify-content:center;gap:34px;font-size:15px;font-weight:600;letter-spacing:.5px}
.hero{top:205px;left:0;width:1200px;height:501px;background:#000}
.photo{position:absolute;overflow:hidden}
.band{position:absolute;left:0;right:0;bottom:0;height:74px;background:var(--band);font-family:"Playfair Display",serif;color:var(--band-text);white-space:nowrap}
.band span{position:absolute;top:50%;transform:translateY(-50%);line-height:1}
.band .who{left:18px;font-size:38px}
.band .brand{left:50%;transform:translate(-50%,-50%);font-size:26px;letter-spacing:1px}
.band .brand.lead{left:40px;transform:translateY(-50%)}
.band .town{right:18px;font-size:22px}
.card .band{height:66px}
.card .band .who{font-size:34px}
.card .band .town{font-size:20px}
.card .band .brand{font-size:24px}
.cat{top:715px;width:231px;height:183px}
.cat-label{top:917px;width:231px;text-align:center;font-size:17px;white-space:nowrap}
.focus-head{top:1050px;left:0;width:1200px;text-align:center}
.focus-head .line{width:126px;height:2px;background:var(--accent-line);margin:0 auto}
.focus-head h2{font-size:35px;font-weight:400;letter-spacing:.5px;margin:22px 0 18px}
.focus-head h2 b{font-weight:700}
.card{width:451px;height:451px}
.promo{top:2227px;left:0;width:1200px;height:543px;background:linear-gradient(180deg,var(--brown-top),var(--brown-mid) 55%,#c0916d)}
.promo-text{left:688px;top:2318px;color:var(--white)}
.promo-text .t1{font-size:33px;font-weight:400;line-height:36px}
.promo-text .t2{font-size:44px;font-weight:700;line-height:48px}
.promo-text p{margin-top:34px;font-family:"Hind",sans-serif;font-size:24px;font-weight:700;line-height:33px;color:var(--promo-copy);white-space:nowrap}
.apply{left:691px;top:2595px;width:122px;height:54px;border:2px solid var(--white);color:var(--white);font-size:15px;font-weight:600;display:flex;align-items:center;justify-content:center}
.social{top:2823px;left:918px;display:flex;gap:5px}
.social span{width:33px;height:33px;border-radius:50%;background:var(--ink);display:block}
.foot-text{right:174px;text-align:right;font-size:14px;line-height:23px;white-space:nowrap}
</style>
</head>
<body>

<header>
  <div class="abs icon-dot" style="left:172px;top:18px">
    <svg width="17" height="17" viewBox="0 0 24 24"><path fill="#fff" d="M6.6 10.8a15 15 0 0 0 6.6 6.6l2.2-2.2a1 1 0 0 1 1-.25 11.4 11.4 0 0 0 3.6.57 1 1 0 0 1 1 1V20a1 1 0 0 1-1 1A17 17 0 0 1 3 4a1 1 0 0 1 1-1h3.5a1 1 0 0 1 1 1c0 1.25.2 2.45.57 3.57a1 1 0 0 1-.25 1z"/></svg>
  </div>
  <div class="abs contact" style="left:172px;top:61px">+44 700 555 01 42<br>+90 500 555 38 19</div>

  <div class="abs logo" style="left:450px;top:28px;width:300px">
    <div class="name">LUNA</div>
    <div class="sub">MODEL MGMT</div>
  </div>

  <div class="abs icon-dot" style="left:820px;top:18px">
    <svg width="18" height="14" viewBox="0 0 24 18"><rect x="1.5" y="1.5" width="21" height="15" rx="2" fill="none" stroke="#fff" stroke-width="2"/><path d="M2 3l10 7 10-7" fill="none" stroke="#fff" stroke-width="2"/></svg>
  </div>
  <div class="abs contact" style="left:821px;top:61px">Mail:<br>Booker@lunafaces.com</div>

  <div class="abs rule"></div>
  <nav class="abs nav">
    <span>HOME</span><span>LONDON</span><span>PARIS</span><span>ISTANBUL</span><span>MILAN</span><span>ATHENS</span><span>DUBAI</span><span>CONTACT</span>
  </nav>
</header>

<section class="abs hero">
  <div class="photo" style="left:0;top:12px;width:338px;height:480px;background:linear-gradient(135deg,#a89a8a,#c9b7a3 50%,#8c7f72)" role="img" aria-label="Close-up portrait of a female model">
    <div class="band"><span class="brand lead">LUNA MODELS</span><span class="town">In Town</span></div>
  </div>
  <div class="photo" style="left:347px;top:12px;width:480px;height:480px;background:linear-gradient(160deg,#d9d9d6,#c9cbc6 40%,#4f8a5a 70%,#d0d0cc)" role="img" aria-label="Female model in a green tropical print outfit">
    <div class="band"><span class="who">Amara</span><span class="brand">LUNA MODELS</span><span class="town">In Town</span></div>
  </div>
  <div class="photo" style="left:836px;top:12px;width:364px;height:480px;background:linear-gradient(150deg,#9aa0a6,#c7c4be 45%,#4a4038 80%)" role="img" aria-label="Smiling female model walking on a city street">
    <div class="band"><span class="who">Delia</span><span class="brand" style="left:auto;right:10px;transform:translateY(-50%)">LUNA MODELS</span></div>
  </div>
</section>

<section>
  <div class="abs cat" style="left:9px;background:linear-gradient(135deg,#e8dccd,#d3b99b)" role="img" aria-label="Women category portrait"></div>
  <div class="abs cat" style="left:247px;background:linear-gradient(135deg,#9a9a9a,#e0e0e0 60%,#666)" role="img" aria-label="Men category portrait"></div>
  <div class="abs cat" style="left:485px;background:linear-gradient(135deg,#cfcfcf,#7a7a7a 60%,#2a2a2a)" role="img" aria-label="Women development portrait"></div>
  <div class="abs cat" style="left:724px;background:linear-gradient(135deg,#bdbdbd,#3d3d3d 55%,#8a8a8a)" role="img" aria-label="Men development portrait"></div>
  <div class="abs cat" style="left:961px;background:linear-gradient(135deg,#6f8a4a,#c8a06a 50%,#2f5c52)" role="img" aria-label="Talent category portrait"></div>
  <div class="abs cat-label" style="left:9px">WOMEN</div>
  <div class="abs cat-label" style="left:247px">MEN</div>
  <div class="abs cat-label" style="left:485px">WOMEN DEVELOPMENT</div>
  <div class="abs cat-label" style="left:724px">MEN DEVELOPMENT</div>
  <div class="abs cat-label" style="left:961px">TALENT</div>
</section>

<section>
  <svg class="abs" style="left:930px;top:1080px" width="230" height="240" viewBox="0 0 230 240"><path d="M20 120 L102 38 L184 120" fill="none" stroke="var(--deco)" stroke-width="7"/></svg>
  <svg class="abs" style="left:70px;top:2040px" width="140" height="140" viewBox="0 0 140 140"><circle cx="70" cy="70" r="62" fill="none" stroke="var(--deco)" stroke-width="8"/></svg>

  <div class="abs focus-head">
    <div class="line"></div>
    <h2>MODELS <b>IN FOCUS</b></h2>
    <div class="line"></div>
  </div>

  <div class="abs photo card" style="left:130px;top:1183px;background:linear-gradient(120deg,#e9e9e9,#b0b0b0 45%,#1e1e1e 80%)" role="img" aria-label="Male model in a black leather jacket">
    <div class="band"><span class="who">Matteo</span><span class="brand">LUNA MODELS</span><span class="town">In Town</span></div>
  </div>
  <div class="abs photo card" style="left:617px;top:1183px;background:linear-gradient(120deg,#6a5236,#c9a06a 45%,#e0c48e 75%,#a88452)" role="img" aria-label="Female model in a cream dress in warm light">
    <div class="band"><span class="who">Irina V</span><span class="brand">LUNA MODELS</span><span class="town">In Town</span></div>
  </div>
  <div class="abs photo card" style="left:130px;top:1677px;background:linear-gradient(135deg,#1a1a1a,#8a8a8a 50%,#2a2a2a)" role="img" aria-label="Black and white portrait of a female model">
    <div class="band"><span class="who">Irina V</span><span class="brand">LUNA MODELS</span><span class="town">In Town</span></div>
  </div>
  <div class="abs photo card" style="left:617px;top:1677px;background:linear-gradient(135deg,#2a1d14,#8a6a50 45%,#3a2a20 80%)" role="img" aria-label="Male model in a dark turtleneck">
    <div class="band"><span class="who">Rafael</span><span class="brand">LUNA MODELS</span><span class="town">In Town</span></div>
  </div>
</section>

<section class="abs promo"></section>
<div class="abs photo" style="left:172px;top:2260px;width:479px;height:479px;background:linear-gradient(135deg,#e8e6e2,#9a8070 45%,#3a2a22 75%,#d8d4cf)" role="img" aria-label="Close-up portrait of a male model">
  <div class="band"><span class="who">Matteo</span><span class="brand">LUNA MODELS</span><span class="town">In Town</span></div>
</div>
<div class="abs promo-text">
  <div class="t1">MODELS</div>
  <div class="t2">IN FOCUS</div>
  <p>JOIN A GLOBAL AGENCY THAT<br>REPRESENTS SOME OF THE<br>BIGGEST NAMES IN THE MODEL<br>INDUSTRY.</p>
</div>
<div class="abs apply">APPLY NOW</div>

<footer>
  <div class="abs logo" style="left:160px;top:2838px;width:200px">
    <div class="name">LUNA</div>
    <div class="sub">MODEL MGMT</div>
  </div>
  <div class="abs social"><span></span><span></span><span></span></div>
  <div class="abs foot-text" style="top:2878px">Unit 118, Floor 9th, A Blok, Meridyen Tower,<br>Deniz Local, Kavak, Istanbul, Turkey</div>
  <div class="abs foot-text" style="top:2939px">Luna Model Agency © 2021</div>
</footer>

</body>
</html>
```